Welcome Series Email: 1st Email in Series BargainLifts.net

I am working to create a three part welcome series email for visitors to my website but I need a little help getting a creative look and feel that looks professional. I am just looking for some help with the design of the 1st email that we can then develop the first email with and pass down some of the creative elements to the next two emails in the series. My site is BargainLifts.net and we sell a broad range of products from motorcycle all the way to wheelchair and mobility so I need to be mindful of all the different customer types. I have a prototype of the 1st email that my email service provider created that is attached and I just am not happy with the design. I would be interested if someone could take the general concept of this email and give it better look. If you have a completely different idea I am open to that as well. The design I choose does not have to be the perfect final product just a great shell that will dictate the look and feel of all emails I send to my customer list.
Thanks for your help!

```html
<!DOCTYPE html>
<html lang="en">
<head>
<meta charset="utf-8">
<title>BargainLifts.net – Welcome Email</title>
<link href="https://fonts.googleapis.com/css2?family=Raleway:wght@400;500;600&family=Open+Sans:wght@400;600&display=swap" rel="stylesheet">
<style>
  :root {
    --brand-blue: #2b3b8f;
    --hero-blue: #33459f;
    --navy: #1c2456;
    --brand-red: #c8161d;
    --ink: #3a3a3a;
    --muted: #777777;
    --rule: #dddddd;
    --band: #f3f3f3;
    --white: #ffffff;
    --icon-grey: #9a9a9a;
  }
  * { margin: 0; padding: 0; box-sizing: border-box; }
  html, body { width: 956px; height: 1200px; overflow: hidden; background: var(--white); }
  body { position: relative; font-family: "Open Sans", sans-serif; color: var(--ink); }
  .abs { position: absolute; }
  .center { left: 0; width: 956px; text-align: center; }

  /* header */
  .header { top: 0; left: 0; width: 956px; height: 94px; }
  .brand-name { top: 34px; font-family: "Raleway", sans-serif; font-weight: 600; font-size: 24px; color: var(--brand-blue); }
  .social { top: 62px; left: 766px; display: flex; gap: 10px; }
  .social span { width: 14px; height: 14px; border-radius: 50%; background: var(--icon-grey); display: block; }

  /* hero */
  .hero { top: 94px; left: 0; width: 956px; height: 376px; background: linear-gradient(135deg, #3b4ea8 0%, #2f4199 50%, #3e52a6 100%); }
  .hero-title { top: 110px; font-family: "Raleway", sans-serif; font-weight: 500; font-size: 32px; color: var(--white); letter-spacing: 0.3px; }
  .hero-sub { top: 150px; font-family: "Raleway", sans-serif; font-weight: 500; font-size: 15.5px; color: var(--white); }
  .hero-copy { top: 178px; left: 228px; width: 500px; text-align: center; font-size: 8.6px; line-height: 13px; color: #c9d0ec; }
  .btn { top: 213px; height: 27px; font-family: "Raleway", sans-serif; font-weight: 500; font-size: 11px; color: var(--white); display: flex; align-items: center; justify-content: center; }
  .btn-primary { left: 372px; width: 103px; background: var(--navy); }
  .btn-accent { left: 482px; width: 103px; background: var(--brand-red); }
  .dots { top: 357px; left: 460px; display: flex; gap: 3px; }
  .dots span { width: 9px; height: 9px; border-radius: 50%; background: #2a3570; }
  .dots span.active { background: var(--white); }

  /* intro */
  .intro-title { top: 508px; font-family: "Raleway", sans-serif; font-size: 25px; color: var(--brand-red); }
  .intro-lead { top: 544px; font-family: "Raleway", sans-serif; font-size: 11.5px; color: var(--ink); }
  .intro-copy { top: 564px; left: 168px; width: 620px; text-align: center; font-size: 8.8px; line-height: 13px; color: var(--muted); }

  /* categories */
  .categories { top: 636px; left: 0; width: 956px; height: 277px; background: var(--band); border-top: 1px solid var(--rule); border-bottom: 1px solid var(--rule); }
  .cat-title { top: 30px; font-family: "Raleway", sans-serif; font-size: 18px; color: #555; }
  .cat { top: 77px; width: 160px; margin-left: -80px; text-align: center; }
  .cat-photo { width: 122px; height: 122px; margin: 0 auto; border-radius: 50%; border: 4px solid var(--white); box-shadow: 0 0 0 1px #e0e0e0; }
  .cat-name { margin-top: 7px; font-family: "Raleway", sans-serif; font-size: 13px; color: #333; }
  .cat-desc { margin-top: 2px; font-size: 8.8px; color: var(--muted); }
  .arrow { top: 112px; }

  /* benefits */
  .benefit-title { top: 964px; left: 101px; font-family: "Raleway", sans-serif; font-size: 21px; color: var(--brand-blue); }
  .benefit-lead { top: 994px; left: 101px; width: 340px; font-size: 10px; line-height: 16px; color: var(--muted); }
  .benefit-copy { top: 1035px; left: 101px; width: 350px; font-size: 8.3px; line-height: 13px; color: var(--muted); }
  .features { top: 969px; left: 484px; width: 345px; height: 97px; display: flex; background: #f8f8f8; border: 1px solid var(--rule); box-shadow: 0 8px 10px -6px rgba(0,0,0,0.12); }
  .feature { flex: 1; border-right: 1px solid var(--rule); display: flex; flex-direction: column; align-items: center; padding-top: 18px; }
  .feature:last-child { border-right: none; }
  .feature-label { margin-top: 8px; font-family: "Raleway", sans-serif; font-size: 11.5px; line-height: 15px; text-align: center; color: var(--brand-blue); }
  .feature-label.red { color: var(--brand-red); }

  /* footer */
  .footer { top: 1120px; left: 0; width: 956px; height: 80px; border-top: 1px solid var(--rule); background: #fafafa; }
  .footer-links { top: 22px; left: 97px; font-size: 10px; color: #333; }
  .footer-legal { top: 23px; left: 585px; font-size: 9px; color: var(--muted); }
  .footer-copy { top: 43px; left: 97px; font-size: 8.8px; color: var(--muted); }
</style>
</head>
<body>

  <header class="abs header">
    <div class="abs center brand-name">BargainLifts.net</div>
    <div class="abs social" aria-label="Social links"><span></span><span></span><span></span><span></span></div>
  </header>

  <section class="abs hero" role="img" aria-label="Photo of a man loading a motorcycle up a ramp into a pickup truck, tinted blue">
    <h1 class="abs center hero-title">MAURIS LACUS VITAE VESTIBULUM</h1>
    <h2 class="abs center hero-sub">ETIAM NUNC VENENATIS IN TRISTIQUE IMPERDIET NISL</h2>
    <p class="abs hero-copy">Morbi porta libero id ullamcorper nonummy nibh ligula pulvinar metus eget consectetuer augue nisi quis lacus Ut ac mi quis lacus mollis aliquam Curabitur iaculis tempus eros Curabitur vel mi sit amet magn</p>
    <div class="abs btn btn-primary">Learn More</div>
    <div class="abs btn btn-accent">Get Newsletter</div>
    <div class="abs dots"><span class="active"></span><span></span><span></span></div>
  </section>

  <h2 class="abs center intro-title">Vivamus porttitor purus nisi eleifend libero</h2>
  <p class="abs center intro-lead">Morbi diam mauris viverra in gravida eu mattis in ante Morbi eget arcu Morbi porta libero id ullamcorper nonummy</p>
  <p class="abs intro-copy">Morbi porta libero id ullamcorper nonummy nibh ligula pulvinar metus eget consectetuer augue nisi quis lacus Ut ac mi quis lacus mollis aliquam Curabitur iaculis tempus eros Curabitur vel mi sit amet magna malesuada ultrices Ut nisi erat fermentum vel congue</p>

  <section class="abs categories">
    <h3 class="abs center cat-title">Ramps for just About any Occation</h3>
    <svg class="abs arrow" style="left:86px" width="26" height="58" viewBox="0 0 26 58"><polyline points="24,2 2,29 24,56" fill="none" stroke="#999" stroke-width="1.5"/></svg>
    <div class="abs cat" style="left:213px">
      <div class="cat-photo" role="img" aria-label="Red sport motorcycle close-up" style="background:radial-gradient(circle at 40% 45%, #e8282a, #a01418 60%, #d9dde3 100%)"></div>
      <div class="cat-name">Power Sports</div>
      <div class="cat-desc">Msan vestibulum commodo</div>
    </div>
    <div class="abs cat" style="left:395px">
      <div class="cat-photo" role="img" aria-label="Wheelchair wheel on pavement" style="background:radial-gradient(circle at 50% 45%, #6b7a8c, #2c333d 60%, #9aa3ad 100%)"></div>
      <div class="cat-name">Mobility</div>
      <div class="cat-desc">Msan vestibulum commodo</div>
    </div>
    <div class="abs cat" style="left:578px">
      <div class="cat-photo" role="img" aria-label="Yellow mobile crane truck" style="background:linear-gradient(180deg, #cfe0ef 0%, #e3c23a 45%, #6e6a5e 100%)"></div>
      <div class="cat-name">Commecial Heavy Duty</div>
      <div class="cat-desc">Msan vestibulum commodo</div>
    </div>
    <div class="abs cat" style="left:759px">
      <div class="cat-photo" role="img" aria-label="Car wheel and headlight at sunset" style="background:radial-gradient(circle at 60% 30%, #e7c79a, #5a6370 55%, #2a2f38 100%)"></div>
      <div class="cat-name">Automotive</div>
      <div class="cat-desc">Msan vestibulum commodo</div>
    </div>
    <svg class="abs arrow" style="left:843px" width="26" height="58" viewBox="0 0 26 58"><polyline points="2,2 24,29 2,56" fill="none" stroke="#999" stroke-width="1.5"/></svg>
  </section>

  <h2 class="abs benefit-title">Curabitur iaculis tempus eros vel sit</h2>
  <p class="abs benefit-lead">As a member of our special email program you will be the first to hear about new products, exclusive offers and upcoming sales events.</p>
  <p class="abs benefit-copy">Morbi porta libero id ullamcorper nonummy nibh ligula pulvinar metus eget consectetuer augue nisi quis lacus Ut ac mi quis lacus mollis aliquam Curabitur iaculis tempus eros Curabitur vel mi sit amet magna malesuada</p>

  <div class="abs features">
    <div class="feature">
      <svg width="44" height="36" viewBox="0 0 44 36"><path d="M4 4 L20 4 L40 22 L28 34 L8 16 Z" fill="var(--brand-blue)" transform="rotate(0)"/><circle cx="11" cy="10" r="2.5" fill="#f8f8f8"/></svg>
      <div class="feature-label">Discount Prices</div>
    </div>
    <div class="feature">
      <svg width="44" height="36" viewBox="0 0 44 36"><rect x="4" y="4" width="24" height="22" rx="2" fill="var(--brand-red)"/><path d="M28 11 H36 L41 18 V26 H28 Z" fill="var(--brand-red)"/><circle cx="12" cy="28" r="4.5" fill="var(--brand-red)" stroke="#f8f8f8" stroke-width="2"/><circle cx="34" cy="28" r="4.5" fill="var(--brand-red)" stroke="#f8f8f8" stroke-width="2"/></svg>
      <div class="feature-label red">Fast Shipping</div>
    </div>
    <div class="feature">
      <svg width="44" height="36" viewBox="0 0 44 36"><rect x="2" y="4" width="40" height="26" rx="2" fill="var(--brand-blue)"/><rect x="7" y="9" width="30" height="16" fill="#f8f8f8"/><circle cx="22" cy="17" r="7" fill="var(--brand-blue)"/><text x="22" y="21" font-family="Open Sans, sans-serif" font-size="10" font-weight="600" fill="#f8f8f8" text-anchor="middle">1</text></svg>
      <div class="feature-label">100% Money<br>Back Guarantee</div>
    </div>
  </div>

  <footer class="abs footer">
    <div class="abs footer-links">Wheelchair &amp; Mobility &nbsp;| &nbsp;Powerparts &nbsp;| &nbsp;Automotive &nbsp;| &nbsp;Recreation &nbsp;| &nbsp;Pet &nbsp;| &nbsp;Commecial &amp; Usbility</div>
    <div class="abs footer-legal">Privacy Policy &nbsp;| &nbsp;Unsubscribe from receiving future communication</div>
    <div class="abs footer-copy">© 2014 Company Name &nbsp;All right reserved &nbsp;Term of Use</div>
  </footer>

</body>
</html>
```